Business Card Design

We need elegant business card design. We are conglomerate for different businesses. Nature of our businesses include Construction, Health care, Energy and Automotive

Target Market(s)

Business to business clients ages 40+

Industry/Entity Type

Automotive

Contact Information for Business Card

Darian (Dax) Kellum
CEO
Brightpath Group of Companies, Inc
3917 Larkmoor Rd E, Houston, TX, 77431
C:832-406-1357 O: 281-739-4016 F: 281-612-9548

```html
<!DOCTYPE html>
<html lang="en">
<head>
<meta charset="utf-8">
<title>Brightpath Group of Companies – Business Card</title>
<link rel="stylesheet" href="https://fonts.googleapis.com/css2?family=Marcellus+SC&family=Josefin+Sans:wght@400;600&display=swap">
<style>
  :root {
    --backdrop: #2b2b2b;
    --card: #ffffff;
    --ink: #111111;
    --ink-soft: #2a2a2a;
  }
  html, body {
    margin: 0;
    padding: 0;
    width: 1200px;
    height: 800px;
    overflow: hidden;
    background: var(--backdrop);
  }
  .canvas {
    width: 1200px;
    height: 800px;
    display: flex;
    align-items: center;
    justify-content: center;
  }
  .business-card {
    position: relative;
    width: 840px;
    height: 480px;
    background: var(--card);
    color: var(--ink);
    box-sizing: border-box;
  }
  .company-name {
    position: absolute;
    top: 78px;
    left: 0;
    right: 0;
    margin: 0;
    text-align: center;
    font-family: "Marcellus SC", serif;
    font-weight: 400;
    font-size: 29px;
    letter-spacing: 0.16em;
  }
  .sector-icons {
    position: absolute;
    top: 168px;
    left: 80px;
    right: 80px;
    display: flex;
    justify-content: space-around;
    align-items: center;
    height: 90px;
  }
  .sector-icon {
    width: 76px;
    height: 76px;
    fill: var(--ink);
  }
  .sector-icon--outline {
    fill: none;
    stroke: var(--ink);
    stroke-width: 3;
    stroke-linecap: round;
    stroke-linejoin: round;
  }
  .contact-block {
    position: absolute;
    left: 64px;
    bottom: 62px;
    font-family: "Josefin Sans", sans-serif;
    color: var(--ink-soft);
  }
  .contact-name {
    margin: 0 0 10px;
    font-size: 27px;
    font-weight: 600;
    font-variant: small-caps;
    letter-spacing: 0.01em;
    color: var(--ink);
  }
  .contact-title {
    font-weight: 400;
  }
  .contact-line {
    margin: 0 0 4px;
    font-size: 17px;
    font-variant: small-caps;
  }
  .contact-line--phones {
    font-variant: normal;
    font-size: 17px;
  }
</style>
</head>
<body>
<main class="canvas">
  <article class="business-card">
    <h1 class="company-name">Brightpath Group of Companies, Inc</h1>

    <div class="sector-icons">
      <!-- Construction -->
      <svg class="sector-icon" viewBox="0 0 64 64" role="img" aria-label="Construction">
        <rect x="23" y="26" width="9" height="36" rx="3" transform="rotate(35 27 44)"/>
        <path d="M18 12 L44 12 Q54 14 58 22 Q50 18 44 20 L44 26 L18 26 Z" transform="rotate(35 32 20)"/>
      </svg>
      <!-- Automotive -->
      <svg class="sector-icon" viewBox="0 0 64 64" role="img" aria-label="Automotive">
        <path d="M14 16 Q16 10 22 10 L42 10 Q48 10 50 16 L54 28 Q60 30 60 36 L60 48 L4 48 L4 36 Q4 30 10 28 Z M18 17 L15 27 L49 27 L46 17 Q45 15 42 15 L22 15 Q19 15 18 17 Z M12 34 a4 4 0 1 0 0.1 0 Z M52 34 a4 4 0 1 0 0.1 0 Z M22 38 L42 38 L42 42 L22 42 Z" fill-rule="evenodd"/>
        <rect x="6" y="46" width="10" height="10" rx="2"/>
        <rect x="48" y="46" width="10" height="10" rx="2"/>
      </svg>
      <!-- Energy -->
      <svg class="sector-icon sector-icon--outline" viewBox="0 0 64 64" role="img" aria-label="Energy">
        <path d="M24 44 Q24 38 19 32 Q14 26 16 18 Q20 6 32 6 Q44 6 48 18 Q50 26 45 32 Q40 38 40 44 Z"/>
        <path d="M28 44 L28 28 Q26 22 30 22 Q32 24 32 28 Q32 24 34 22 Q38 22 36 28 L36 44"/>
        <line x1="24" y1="49" x2="40" y2="49"/>
        <line x1="25" y1="54" x2="39" y2="54"/>
        <line x1="28" y1="59" x2="36" y2="59"/>
      </svg>
      <!-- Health care -->
      <svg class="sector-icon" viewBox="0 0 64 64" role="img" aria-label="Health care">
        <g transform="rotate(45 32 32)">
          <rect x="27" y="14" width="10" height="30" rx="2"/>
          <rect x="22" y="12" width="20" height="4" rx="1"/>
          <rect x="30" y="2" width="4" height="11"/>
          <rect x="25" y="0" width="14" height="4" rx="1"/>
          <rect x="31" y="44" width="2" height="18"/>
        </g>
      </svg>
    </div>

    <section class="contact-block">
      <p class="contact-name">Darian (Dax) Kellum <span class="contact-title">CEO</span></p>
      <p class="contact-line">3917 Larkmoor Rd E, Houston, TX, 77431</p>
      <p class="contact-line contact-line--phones">C: 832-406-1357 O: 281-739-4016 F: 281-612-9548</p>
    </section>
  </article>
</main>
</body>
</html>
```